VoxMend needs a Letterhead

We need a letterhead for our company "VoxMend Consultants". Logo is attached. The company color is Turquoise. Icons for website, scan logo for website, icons for address, e-mail and phone appreciated rather than just words.

Industry/Entity Type

It Company

```html
<!DOCTYPE html>
<html lang="en">
<head>
<meta charset="utf-8">
<title>VoxMend Consultants – Letterhead Set</title>
<link href="https://fonts.googleapis.com/css2?family=Open+Sans:wght@400;600&display=swap" rel="stylesheet">
<style>
  :root{
    --brand-blue:#2b55a6;
    --brand-green:#7cc242;
    --paper:#ffffff;
    --page-edge:#cfcfcf;
    --divider:#e6e3e3;
    --ink:#3a3a3a;
    --faint-blue:#eef1f8;
    --faint-green:#f2f8ec;
  }
  *{margin:0;padding:0;box-sizing:border-box}
  html,body{width:1200px;height:4202px;overflow:hidden;background:var(--paper)}
  body{position:relative;font-family:"Open Sans",Arial,sans-serif;color:var(--ink)}
  .sheet{position:absolute;left:37px;width:1140px;background:var(--paper);border:2px solid var(--page-edge);box-shadow:0 2px 6px rgba(0,0,0,.18);overflow:hidden}
  .sheet--wave{top:14px;height:1247px}
  .sheet--band{top:1330px;height:1290px}
  .sheet--bar{top:2685px;height:1500px}
  .divider{position:absolute;left:0;width:1200px;height:24px;background:var(--divider)}
  .divider--one{top:1285px}
  .divider--two{top:2645px}
  .brand{position:absolute;display:flex;align-items:center;gap:18px}
  .brand__mark{width:58px;height:58px;background:var(--brand-green)}
  .brand__name{font-weight:600;color:var(--brand-blue);font-size:44px;line-height:1;letter-spacing:.5px;white-space:nowrap}
  .art{position:absolute;left:0;top:0}
  .contact-line{position:absolute;left:0;width:100%;display:flex;justify-content:center;align-items:center;gap:34px;font-size:15px;color:var(--brand-blue);font-weight:600}
  .contact-item{display:flex;align-items:center;gap:8px;white-space:nowrap}
  .icon{width:20px;height:20px;flex:none}
  .icon--home{color:var(--brand-green)}
  .icon--green{color:var(--brand-green)}
  .icon--blue{color:var(--brand-blue)}
  .band-list{position:absolute;display:flex;flex-direction:column;gap:12px;font-size:15px;font-weight:600;color:#fff}
  .band-list .contact-item{gap:12px}
  .band-list .icon{color:#fff}
  .bar-address{position:absolute;right:24px;top:38px;font-size:15px;font-weight:600;color:#fff;white-space:nowrap}
  .watermark{position:absolute;left:60px;top:590px;display:flex;align-items:center;gap:40px}
  .watermark__mark{width:230px;height:300px;background:var(--faint-blue)}
  .watermark__name{font-size:118px;font-weight:600;color:var(--faint-blue);line-height:1;white-space:nowrap}
</style>
</head>
<body>
<svg width="0" height="0" style="position:absolute">
  <defs>
    <symbol id="i-home" viewBox="0 0 20 20"><path d="M10 2 1 10h3v8h5v-5h2v5h5v-8h3z" fill="currentColor"/></symbol>
    <symbol id="i-phone" viewBox="0 0 20 20"><path d="M5 2l3 4-2 2c1 2 4 5 6 6l2-2 4 3-2 3C9 18 2 11 2 4z" fill="currentColor"/></symbol>
    <symbol id="i-fax" viewBox="0 0 20 20"><rect x="5" y="2" width="10" height="5" fill="currentColor"/><rect x="2" y="8" width="16" height="7" rx="1" fill="currentColor"/><rect x="5" y="13" width="10" height="5" fill="currentColor"/></symbol>
    <symbol id="i-mail" viewBox="0 0 20 20"><path d="M3 10l5 5L17 4" fill="none" stroke="currentColor" stroke-width="3" stroke-linecap="round" stroke-linejoin="round"/></symbol>
    <symbol id="i-web" viewBox="0 0 20 20"><circle cx="10" cy="10" r="8" fill="none" stroke="currentColor" stroke-width="2"/><path d="M2 10h16M10 2c-4 4-4 12 0 16M10 2c4 4 4 12 0 16" fill="none" stroke="currentColor" stroke-width="1.5"/></symbol>
  </defs>
</svg>

<!-- Letterhead 1: wave header -->
<section class="sheet sheet--wave">
  <svg class="art" width="1140" height="200" viewBox="0 0 1140 200">
    <path d="M0 0H360V20C300 70 180 130 0 150Z" fill="var(--brand-green)"/>
    <path d="M370 0H1140V120C1000 80 880 60 760 90C620 120 500 90 370 40Z" fill="var(--brand-blue)"/>
  </svg>
  <div class="brand" style="left:300px;top:95px">
    <span class="brand__mark"></span>
    <span class="brand__name">VoxMend Consultants</span>
  </div>
  <div class="contact-line" style="top:1158px">
    <span class="contact-item"><svg class="icon icon--home"><use href="#i-home"/></svg>24 Harbor Lane, Suite 8, Portland OR 97201</span>
  </div>
  <div class="contact-line" style="top:1190px">
    <span class="contact-item"><svg class="icon icon--green"><use href="#i-phone"/></svg>555 210 4400</span>
    <span class="contact-item"><svg class="icon icon--green"><use href="#i-fax"/></svg>555 210 4401</span>
    <span class="contact-item"><svg class="icon icon--green"><use href="#i-mail"/></svg>hello@voxmend.com</span>
    <span class="contact-item"><svg class="icon icon--green"><use href="#i-web"/></svg>www.voxmend.com</span>
  </div>
</section>

<div class="divider divider--one"></div>

<!-- Letterhead 2: diagonal footer band -->
<section class="sheet sheet--band">
  <div class="brand" style="left:330px;top:95px">
    <span class="brand__mark"></span>
    <span class="brand__name">VoxMend Consultants</span>
  </div>
  <svg class="art" style="top:1100px" width="1140" height="190" viewBox="0 0 1140 190">
    <rect width="1140" height="190" fill="var(--brand-green)"/>
    <path d="M0 0H500L640 190H0Z" fill="var(--brand-blue)"/>
  </svg>
  <div class="band-list" style="left:40px;top:1120px">
    <span class="contact-item"><svg class="icon"><use href="#i-phone"/></svg>555 210 4400</span>
    <span class="contact-item"><svg class="icon"><use href="#i-fax"/></svg>555 210 4401</span>
    <span class="contact-item"><svg class="icon"><use href="#i-mail"/></svg>hello@voxmend.com</span>
    <span class="contact-item"><svg class="icon"><use href="#i-web"/></svg>www.voxmend.com</span>
  </div>
  <div class="band-list" style="left:860px;top:1160px">
    <span class="contact-item"><svg class="icon"><use href="#i-home"/></svg>24 Harbor Lane, Suite 8</span>
    <span class="contact-item" style="padding-left:32px">Portland, Oregon</span>
    <span class="contact-item" style="padding-left:32px">OR 97201, USA</span>
  </div>
</section>

<div class="divider divider--two"></div>

<!-- Letterhead 3: top bar with watermark -->
<section class="sheet sheet--bar">
  <svg class="art" width="1140" height="80" viewBox="0 0 1140 80">
    <rect x="0" y="0" width="140" height="40" fill="var(--brand-green)"/>
    <rect x="140" y="28" width="1000" height="42" fill="var(--brand-blue)"/>
  </svg>
  <div class="bar-address">24 Harbor Lane, Suite 8, Portland, Oregon OR 97201, USA</div>
  <div class="brand" style="left:60px;top:180px">
    <span class="brand__mark"></span>
    <span class="brand__name">VoxMend Consultants</span>
  </div>
  <div class="watermark">
    <span class="watermark__mark"></span>
    <span class="watermark__name">VoxMend</span>
  </div>
  <div class="contact-line" style="top:1440px">
    <span class="contact-item"><svg class="icon icon--green"><use href="#i-phone"/></svg>555 210 4400</span>
    <span class="contact-item"><svg class="icon icon--green"><use href="#i-fax"/></svg>555 210 4401</span>
    <span class="contact-item"><svg class="icon icon--green"><use href="#i-mail"/></svg>hello@voxmend.com</span>
    <span class="contact-item"><svg class="icon icon--green"><use href="#i-web"/></svg>www.voxmend.com</span>
  </div>
</section>
</body>
</html>
```